Logo/Stationary for Personal Injury Law Firm

We need a logo for our firm and stationary (letterhead, business cards, envelopes) to feature it. We are a personal injury firm that is branching off and starting on our own. Our firm name is "Halloway Law, P.C." We would like to take a more modern approach with the design, but still look professional. Our firm takes a very personal approach with all of our clients.
Updates
Here is the info located in the supported file (if you couldnt access it): 4127 North Bramble Street Oklahoma City, Oklahoma 73254 Telephone: (405) 362-4817 Fax: (405) 362-4930 Toll Free: (866) 362-4817 Website: www.HallowayLaw.example Email: name@hallowaylaw.example Attorneys: Gideon Halloway – licensed to practice in Oklahoma Colin Pratchett – licensed to practice in Oklahoma Of Counsel Desmond Quill – licensed to practice in Texas Enzo Farraday – licensed to practice in New York
Halloway Law, P.C.
I have attached an example of the letterhead from our old firm. The main attorneys (Gideon & Colin) should come first and the of counsel attorneys should be second because they just assist with cases. But please don't let this example box you in to a certain concept.
Target Market(s)
Potential clients involved in personal injury cases (auto accidents, pharmaceutical litigation, medical malpractice & nursing home negligence).
Industry/Entity Type
Lawyer
Requirements
Must have
- Logo - Firm name "Halloway Law, P.C."
- Letterhead - Please see the supporting file containing all the information that needs to be presented.
- Business Card - name, title (attorney/legal assistant), address, telephone, fax, email, website
- Envelope - Logo and address
Should not have
- All of the attorneys are male, so we aren''t interested in any feminine designs.
- Please do not use any scales, gavels or family crest designs.

```html
<!DOCTYPE html>
<html lang="en">
<head>
<meta charset="utf-8">
<title>Halloway Law, P.C. — Letterhead</title>
<link href="https://fonts.googleapis.com/css2?family=EB+Garamond:wght@400;600;700&display=swap" rel="stylesheet">
<style>
  :root {
    --ink: #111111;
    --paper: #ffffff;
    --frame: #222222;
    --mark: #b00010;
  }
  * { box-sizing: border-box; margin: 0; padding: 0; }
  html, body { width: 927px; height: 1200px; overflow: hidden; background: var(--paper); }
  .letterhead {
    position: relative;
    width: 927px; height: 1200px;
    border: 1px solid var(--frame);
    font-family: "EB Garamond", Garamond, serif;
    color: var(--ink);
  }
  .brand {
    position: absolute; left: 80px; top: 80px;
    display: flex; align-items: center; gap: 16px;
  }
  .brand-square { width: 40px; height: 40px; background: var(--mark); }
  .brand-name { font-size: 40px; font-weight: 600; line-height: 1; letter-spacing: 0.5px; }
  .contact {
    position: absolute; right: 68px; top: 78px;
    text-align: right;
  }
  .contact-address { font-size: 15.5px; font-weight: 600; line-height: 20px; margin-bottom: 14px; }
  .contact-lines { font-size: 12.5px; line-height: 16.5px; }
  .roster {
    position: absolute; left: 70px; right: 68px; top: 1090px;
    display: grid; grid-template-columns: 211px 211px 180px 1fr;
  }
  .roster-label { font-size: 15px; height: 24px; }
  .attorney-name { font-size: 15.5px; font-weight: 700; line-height: 18px; }
  .attorney-license { font-size: 13.5px; line-height: 17px; }
</style>
</head>
<body>
<div class="letterhead">
  <header class="brand">
    <div class="brand-square"></div>
    <div class="brand-name">Halloway Law, P.C.</div>
  </header>

  <address class="contact" style="font-style:normal">
    <div class="contact-address">
      4127 North Bramble Street<br>
      Oklahoma City, Oklahoma 73254
    </div>
    <div class="contact-lines">
      Telephone: (405) 362-4817<br>
      Fax: (405) 362-4930<br>
      Toll Free: (866) 362-4817<br>
      Website: www.HallowayLaw.example<br>
      Email: name@hallowaylaw.example
    </div>
  </address>

  <footer class="roster">
    <div>
      <div class="roster-label">Attorneys:</div>
      <div class="attorney-name">Gideon Halloway</div>
      <div class="attorney-license">licensed to practice in Oklahoma</div>
    </div>
    <div>
      <div class="roster-label">&nbsp;</div>
      <div class="attorney-name">Colin Pratchett</div>
      <div class="attorney-license">licensed to practice in Oklahoma</div>
    </div>
    <div>
      <div class="roster-label">Of Counsel:</div>
      <div class="attorney-name">Desmond Quill</div>
      <div class="attorney-license">licensed to practice in Texas</div>
    </div>
    <div>
      <div class="roster-label">&nbsp;</div>
      <div class="attorney-name">Enzo Farraday</div>
      <div class="attorney-license">licensed to practice in New York</div>
    </div>
  </footer>
</div>
</body>
</html>
```